Quiet Harbor Health Flyer (new business startup)

One page...clear enough to be read if faxed. This mental health clinic treats depression/anxiety in kids and adults. It also treats opiate and alcohol addiction. It's in downtown Elmira, NY and the owner of the clinic is from Elmira NY, where it's located. This clinic does not take health insurance, so it charges a low rate of $75 a visit once they pay the $125 starting fee.
Updates

Slow in providing feedback

Target Market(s)

doctors offices, new patients

Industry/Entity Type

Doctor

Requirements
Must have
• see microsoft word document. pdf is printed on the company letterhead.
Nice to have
• a simplified map would be nice. if you can include the building it would be a plus. The same two fonts were used in the business cards and letter head (kennedy small caps boo*) and Refrigerator Delux.

```html
<!DOCTYPE html>
<html lang="en">
<head>
<meta charset="utf-8">
<title>Quiet Harbor Health Flyer</title>
<link rel="stylesheet" href="https://fonts.googleapis.com/css2?family=Lato:wght@400;700;900&display=swap">
<style>
  :root {
    --paper: #f4f7fa;
    --ink: #4a4d52;
    --ink-dark: #2f3236;
    --accent-orange: #d9541e;
    --band-orange: #e8962a;
    --band-blue: #2f86cf;
    --rule-blue: #3a95dc;
    --divider: #7d8087;
    --sky-top: #7fa9d6;
    --brick: #8a5a48;
    --map-light: #e9ecef;
    --map-water: #a9cdeb;
    --arrow-red: #d42a22;
  }
  * { box-sizing: border-box; margin: 0; padding: 0; }
  html, body { width: 1120px; height: 1200px; overflow: hidden; }
  body {
    background: var(--paper);
    font-family: "Lato", Arial, sans-serif;
    color: var(--ink);
    position: relative;
  }
  .header-art { position: absolute; left: 0; top: 0; width: 1120px; height: 660px; }

  .left-column { position: absolute; left: 40px; top: 625px; width: 520px; }

  .pricing { text-align: center; }
  .price-item { font-weight: 700; font-size: 30px; line-height: 1.12; color: var(--ink); }
  .price-item + .price-item { margin-top: 14px; }
  .price-item .amount { color: var(--ink-dark); }

  .ages-box {
    position: relative; margin: 34px auto 0; width: 470px;
    border: 3px solid var(--accent-orange); text-align: center; color: var(--accent-orange);
    padding: 22px 10px 10px;
  }
  .ages-box .ages-title {
    position: absolute; left: 50%; top: -20px; transform: translateX(-50%);
    background: var(--paper); padding: 0 8px; font-size: 28px; font-weight: 400; line-height: 1.2; white-space: nowrap;
  }
  .ages-box .conditions { font-size: 17px; line-height: 1.3; font-weight: 700; }

  .notes { margin: 26px 0 0 45px; width: 430px; font-size: 12px; line-height: 1.35; color: var(--ink); }
  .notes .motto { margin-bottom: 12px; }

  .column-divider { position: absolute; left: 590px; top: 640px; width: 3px; height: 370px; background: var(--divider); }

  .contact { position: absolute; left: 680px; top: 688px; width: 420px; color: var(--ink-dark); }
  .contact .hours { font-size: 22px; font-weight: 700; line-height: 1.22; }
  .contact .rule { width: 320px; height: 4px; background: var(--rule-blue); margin: 11px 0; }
  .contact-line { display: flex; align-items: flex-start; gap: 14px; font-size: 22px; font-weight: 700; line-height: 1.22; margin-bottom: 7px; }
  .contact-line svg { flex: none; margin-top: 2px; }
  .contact .web { font-size: 22px; font-weight: 700; line-height: 1.3; }

  .footer-rule { position: absolute; left: 0; top: 1035px; width: 1120px; height: 5px; background: var(--rule-blue); }
  .brand { position: absolute; left: 0; top: 1080px; width: 1120px; display: flex; justify-content: center; align-items: center; gap: 20px; }
  .brand-dot { width: 44px; height: 44px; border-radius: 50%; background: var(--accent-orange); }
  .brand-name { font-size: 48px; font-weight: 900; color: var(--accent-orange); text-transform: uppercase; letter-spacing: 0.5px; line-height: 1.1; }
</style>
</head>
<body>
  <svg class="header-art" viewBox="0 0 1120 660" xmlns="http://www.w3.org/2000/svg">
    <defs>
      <linearGradient id="buildingTones" x1="0" y1="0" x2="0" y2="1">
        <stop offset="0" stop-color="var(--sky-top)"/>
        <stop offset="0.3" stop-color="#a9b8c8"/>
        <stop offset="0.45" stop-color="var(--brick)"/>
        <stop offset="1" stop-color="#6b5a50"/>
      </linearGradient>
      <linearGradient id="mapTones" x1="0" y1="0" x2="0" y2="1">
        <stop offset="0" stop-color="var(--map-light)"/>
        <stop offset="0.55" stop-color="#dfe4e8"/>
        <stop offset="0.7" stop-color="var(--map-water)"/>
        <stop offset="1" stop-color="#e3e7ea"/>
      </linearGradient>
      <marker id="arrowHead" viewBox="0 0 10 10" refX="5" refY="5" markerWidth="5" markerHeight="5" orient="auto">
        <path d="M0,0 L10,5 L0,10 Z" fill="var(--arrow-red)"/>
      </marker>
    </defs>

    <path class="swoosh-orange" d="M870,0 C1080,50 1120,220 990,350 C860,480 620,520 380,500 L380,515 C640,555 900,500 1050,350 C1140,250 1120,80 1120,0 Z" fill="var(--band-orange)"/>
    <path class="swoosh-blue" d="M0,330 C200,420 420,470 640,470 C820,470 960,420 1040,350 C1000,480 820,560 620,560 C380,560 160,470 0,400 Z" fill="var(--band-blue)"/>

    <g role="img" aria-label="Photo of the clinic's red brick corner building downtown">
      <path d="M0,0 H860 C1050,50 1080,210 970,320 C860,430 640,470 450,455 C280,440 130,400 0,330 Z" fill="url(#buildingTones)"/>
    </g>

    <g role="img" aria-label="Simplified street map of downtown with the clinic location marked">
      <circle cx="880" cy="430" r="188" fill="url(#mapTones)" stroke="var(--band-orange)" stroke-width="8"/>
    </g>

    <path d="M740,430 C655,415 605,345 625,270" fill="none" stroke="var(--arrow-red)" stroke-width="7" stroke-linecap="round" marker-end="url(#arrowHead)"/>
  </svg>

  <div class="left-column">
    <section class="pricing">
      <p class="price-item">Psychiatric Evaluation<br>(45min) .................. <span class="amount">$125*</span></p>
      <p class="price-item">Psychiatric Office Visit<br>(15min) .................. <span class="amount">$75*</span></p>
    </section>

    <section class="ages-box">
      <h2 class="ages-title">Ages: 6 years old and up</h2>
      <p class="conditions">Conditions Treated: Depression, Anxiety,<br>PTSD, ADHD, Addiction, Bipolar,<br>Childhood Mood Disorders</p>
    </section>

    <section class="notes">
      <p class="motto">"We work for you, not the insurance companies"</p>
      <p class="footnote">*Although we do not partner with any Health Insurance Companies at this time, a bill will be provided to you at the time of service for you to submit to your insurance company.</p>
    </section>
  </div>

  <div class="column-divider"></div>

  <section class="contact">
    <p class="hours">Hours:<br>Monday and Saturdays<br>09:00 am to 04:00 pm</p>
    <div class="rule"></div>
    <div class="contact-line">
      <svg width="24" height="34" viewBox="0 0 24 34" aria-hidden="true"><path d="M12,0 C5,0 0,5 0,12 C0,21 12,34 12,34 C12,34 24,21 24,12 C24,5 19,0 12,0 Z" fill="var(--rule-blue)"/><circle cx="12" cy="12" r="5" fill="var(--paper)"/></svg>
      <span>42 Beacon Row #214<br>Elmira, NY 14905</span>
    </div>
    <div class="contact-line">
      <svg width="26" height="26" viewBox="0 0 26 26" aria-hidden="true"><circle cx="13" cy="13" r="13" fill="var(--rule-blue)"/><path d="M8,6 L11,6 L12,10 L10,12 C11,14 12,15 14,16 L16,14 L20,15 L20,18 C20,19 19,20 18,20 C12,20 6,14 6,8 C6,7 7,6 8,6 Z" fill="var(--paper)"/></svg>
      <span>555-014-2231</span>
    </div>
    <div class="contact-line">
      <svg width="26" height="26" viewBox="0 0 26 26" aria-hidden="true"><rect x="6" y="2" width="14" height="7" fill="var(--rule-blue)"/><rect x="1" y="9" width="24" height="11" rx="2" fill="var(--rule-blue)"/><rect x="6" y="16" width="14" height="9" fill="var(--rule-blue)" stroke="var(--paper)" stroke-width="2"/></svg>
      <span>555-014-7788</span>
    </div>
    <div class="rule"></div>
    <p class="web">care@quietharborhealth.com<br>www.quietharborhealth.com</p>
  </section>

  <div class="footer-rule"></div>
  <footer class="brand">
    <div class="brand-dot"></div>
    <span class="brand-name">Quiet Harbor Health</span>
  </footer>
</body>
</html>
```